Business Card Design

A business card design must match as a cleaning company.
We do house cleaning, office, cafe , function center , club and so on.

Industry/Entity Type

House

Contact Information for Business Card

Silver Fern cleaning services
Marla Voss
Director
0429385716
1300 862 419
Silverfern.cleaning@examplemail.com

```html
<!DOCTYPE html>
<html lang="en">
<head>
<meta charset="utf-8">
<title>Silver Fern cleaning services – Business Card</title>
<link rel="stylesheet" href="https://fonts.googleapis.com/css2?family=Jura:wght@500&family=Quicksand:wght@400&family=Play:wght@400;700&display=swap">
<style>
  :root {
    --page-bg: #d9d4cc;
    --card-dark: #1d2419;
    --card-mid: #3d4636;
    --lime: #c6db3a;
    --lime-light: #d9e86a;
    --lime-deep: #a9c21e;
    --brand-text: #cfe03c;
    --ink: #141a10;
    --white: #f3f3ef;
    --tagline: #d6d9d0;
  }
  * { margin: 0; padding: 0; box-sizing: border-box; }
  html, body {
    width: 1200px;
    height: 1000px;
    overflow: hidden;
    background: var(--page-bg);
  }
  .canvas {
    position: relative;
    width: 1200px;
    height: 1000px;
  }
  .business-card {
    position: absolute;
    left: 150px;
    top: 221px;
    width: 900px;
    height: 557px;
    background: radial-gradient(ellipse 60% 55% at 50% 42%, var(--card-mid) 0%, var(--card-dark) 100%);
    box-shadow: 0 10px 30px rgba(0,0,0,0.35);
    overflow: hidden;
  }
  .brand {
    position: absolute;
    left: 190px;
    top: 122px;
    display: flex;
    align-items: center;
    gap: 26px;
  }
  .brand-square {
    width: 62px;
    height: 62px;
    background: var(--white);
  }
  .brand-name {
    font-family: "Jura", sans-serif;
    font-weight: 500;
    font-size: 64px;
    letter-spacing: 5px;
    color: var(--brand-text);
    line-height: 1;
    text-transform: uppercase;
  }
  .brand-tagline {
    position: absolute;
    left: 420px;
    top: 215px;
    font-family: "Quicksand", sans-serif;
    font-size: 27px;
    letter-spacing: 1px;
    color: var(--tagline);
  }
  .info-band {
    position: absolute;
    left: 51px;
    top: 343px;
    width: 793px;
    height: 142px;
    border-top: 3px solid var(--lime);
    border-bottom: 3px solid var(--lime);
    display: flex;
    gap: 6px;
    padding: 6px 0;
  }
  .info-panel {
    background: linear-gradient(180deg, var(--lime-light) 0%, var(--lime) 55%, var(--lime-deep) 100%);
    height: 100%;
  }
  .person-panel {
    width: 392px;
    display: flex;
    flex-direction: column;
    align-items: center;
    justify-content: center;
  }
  .person-name {
    font-family: "Play", sans-serif;
    font-weight: 400;
    font-size: 35px;
    color: var(--ink);
    line-height: 1.1;
  }
  .person-role {
    font-family: "Play", sans-serif;
    font-weight: 700;
    font-size: 20px;
    color: var(--ink);
    margin-top: 4px;
  }
  .contact-panel {
    flex: 1;
    display: flex;
    flex-direction: column;
    justify-content: center;
    gap: 16px;
    padding-left: 28px;
  }
  .contact-line {
    display: flex;
    align-items: center;
    gap: 14px;
    font-family: "Play", sans-serif;
    font-size: 19px;
    color: var(--ink);
    white-space: nowrap;
  }
  .contact-icon { width: 30px; height: 22px; flex: none; }
</style>
</head>
<body>
<main class="canvas">
  <section class="business-card">
    <div class="brand">
      <div class="brand-square"></div>
      <span class="brand-name">Silver Fern</span>
    </div>
    <p class="brand-tagline">cleaning services</p>

    <div class="info-band">
      <div class="info-panel person-panel">
        <p class="person-name">Marla Voss</p>
        <p class="person-role">Director</p>
      </div>
      <div class="info-panel contact-panel">
        <p class="contact-line">
          <svg class="contact-icon" viewBox="0 0 30 22" aria-hidden="true">
            <path d="M2 8 Q2 2 15 2 Q28 2 28 8 L22 8 L21 5 L9 5 L8 8 Z" fill="var(--ink)"/>
            <path d="M7 10 L23 10 L27 20 L3 20 Z" fill="var(--ink)"/>
            <circle cx="15" cy="15" r="3.2" fill="var(--lime)"/>
          </svg>
          0429385716/1300 862 419
        </p>
        <p class="contact-line">
          <svg class="contact-icon" viewBox="0 0 30 22" aria-hidden="true">
            <rect x="2" y="3" width="26" height="17" fill="var(--ink)"/>
            <path d="M2 3 L15 13 L28 3" fill="none" stroke="var(--lime)" stroke-width="1.6"/>
          </svg>
          Silverfern.cleaning@examplemail.com
        </p>
      </div>
    </div>
  </section>
</main>
</body>
</html>
```